website re-design - the brickfern studio

The Brickfern Studio is an existing website that we built using a new zealand based online CMS tool which is quite flexible and accomodates custom designs. You can check it here: http://www.pagequilt.co.nz/.

We have a logo already and the content on the website is OK.
The website can be found at www.thebrickfernstudio.com.au

mainly the homepage, but if the design is easily adapted to the other pages then, we will commission the winner to update these pages also.
Updates

Hi there,  I am uploading an image to be used as the main image on the homepage design,  so all submissions have the same image.

Target Market(s)

property developers, architects, builders, home buyers

Industry/Entity Type

Shop

Requirements
Must have
• Must utilise the existing CMS or at least be compatible to upload
Nice to have
• a promotional banner that can be turned off and on and changed as required as we offer different promotions over time.

```html
<!DOCTYPE html>
<html lang="en">
<head>
<meta charset="utf-8">
<title>The Brickfern Studio – Architectural Scale Models</title>
<link href="https://fonts.googleapis.com/css2?family=Questrial&family=Arimo:wght@400;700&family=Roboto+Condensed:wght@300&display=swap" rel="stylesheet">
<style>
:root{
  --orange:#ef8a2c;
  --orange-dark:#e07a1c;
  --orange-light:#f6a457;
  --ink:#3c3c3c;
  --text:#555;
  --nav:#3d3d3d;
  --nav-dark:#2b2b2b;
  --rule:#dcdcdc;
  --footer:#f0f0f0;
  --red:#c9302a;
  --teal:#2a8a72;
  --green:#4aa64a;
}
*{box-sizing:border-box;margin:0;padding:0}
html,body{width:837px;height:1200px;overflow:hidden}
body{position:relative;background:#fff;font-family:"Questrial",sans-serif;color:var(--text)}
.abs{position:absolute}

.site-header{left:0;top:0;width:837px;height:122px;background:linear-gradient(#f2f2f2,#fff 60%)}
.brand-mark{left:32px;top:24px;width:66px;height:66px;background:var(--orange);border-radius:2px}
.brand-name{left:112px;top:40px;font-size:25px;color:#4a4a4a;letter-spacing:.5px}
.brand-tag{left:113px;top:67px;font-size:12.5px;color:var(--orange);letter-spacing:.6px}
.phone-box{left:586px;top:29px;width:210px;height:51px;background:#fff;border-radius:4px;box-shadow:0 0 6px rgba(0,0,0,.06)}
.phone-box svg{position:absolute;left:14px;top:10px}
.phone-number{position:absolute;left:62px;top:10px;font-size:20px;color:#333;font-family:"Arimo",sans-serif}

.hero-band{left:0;top:122px;width:837px;height:351px;background:linear-gradient(var(--orange-light),var(--orange) 50%,var(--orange-dark))}
.main-nav{left:19px;top:134px;width:801px;height:33px;background:linear-gradient(var(--nav),var(--nav-dark));border-radius:4px;box-shadow:0 1px 2px rgba(0,0,0,.3)}
.main-nav a{position:absolute;top:7px;color:#fff;text-decoration:none;font-family:"Arimo",sans-serif;font-size:14.5px;transform:translateX(-50%);white-space:nowrap}
.hero-frame{left:19px;top:175px;width:801px;height:287px;background:#eee;border-radius:3px}
.hero-image{left:25px;top:181px;width:790px;height:276px;background:linear-gradient(160deg,#9aa29a,#6c7066 40%,#b9a9a0 70%,#5f6a58)}
.hero-caption{left:25px;top:403px;width:790px;height:54px;background:rgba(40,40,40,.55);color:#fff;font-family:"Roboto Condensed",sans-serif;font-weight:300;font-size:29px;padding:8px 0 0 19px}

.intro{left:25px;top:500px;width:530px}
.intro h1{font-weight:400;font-size:18px;color:var(--ink);margin-bottom:18px}
.intro p,.intro li{font-size:11px;line-height:17px}
.intro ol{margin:12px 0 18px 21px}
.divider-v{left:567px;top:490px;width:1px;height:258px;background:var(--rule)}
.why-us{left:592px;top:498px;width:210px}
.why-us h2{font-weight:400;font-size:18px;color:var(--ink);margin-bottom:14px}
.why-image{width:205px;height:113px;background:linear-gradient(90deg,#8e8a82,#a79c8a 50%,#5f6b7c)}
.why-us p{font-size:11px;line-height:16px;margin-top:10px;width:210px}
.read-more{left:725px;top:707px;width:73px;height:21px;background:#444;color:#fff;font-family:"Arimo",sans-serif;font-size:12px;text-align:center;line-height:21px}
.divider-h{left:0;top:749px;width:837px;height:1px;background:var(--rule)}

.services-title{left:33px;top:766px;font-size:18px;color:var(--ink);font-weight:400}
.service-card{top:805px;width:245px;height:250px;border-radius:6px;overflow:hidden;box-shadow:0 0 3px rgba(0,0,0,.35);border:2px solid #f4f4f4}
.service-image{height:154px}
.service-body{height:92px;position:relative;color:#fff;text-align:center}
.service-body h3{font-weight:400;font-size:25px;padding-top:8px}
.service-link{position:absolute;left:5px;bottom:4px;width:227px;height:29px;border-radius:6px;font-family:"Arimo",sans-serif;font-size:11px;line-height:29px;background:rgba(255,255,255,.15)}
.card-commercial{left:32px}
.card-commercial .service-image{background:linear-gradient(#e8f0f4,#a8b8c0 60%,#7fb0c8)}
.card-commercial .service-body{background:linear-gradient(#e0534a,var(--red))}
.card-residential{left:288px}
.card-residential .service-image{background:linear-gradient(#9aa6b2,#2e4e5a 50%,#3d6a48)}
.card-residential .service-body{background:linear-gradient(#3aa58a,var(--teal))}
.card-renovations{left:544px}
.card-renovations .service-image{background:linear-gradient(#cfe0ee,#d8d06a 50%,#8a8a80)}
.card-renovations .service-body{background:linear-gradient(#6cc06a,var(--green))}

.site-footer{left:0;top:1100px;width:837px;height:100px;background:var(--footer);border-top:2px solid #e4e4e4}
.copyright{position:absolute;top:22px;width:100%;text-align:center;font-size:11px;color:#444}
.social{position:absolute;top:51px;width:23px;height:23px;border-radius:3px;background:#8c8c8c}
</style>
</head>
<body>
<header class="abs site-header">
  <div class="abs brand-mark"></div>
  <div class="abs brand-name">THE BRICKFERN STUDIO</div>
  <div class="abs brand-tag">ARCHITECTURAL SCALE MODELS</div>
  <div class="abs phone-box">
    <svg width="34" height="30" viewBox="0 0 34 30" aria-hidden="true">
      <path d="M2 9 Q17 -2 32 9 L29 13 L23 11 L23 8 Q17 5 11 8 L11 11 L5 13 Z" fill="#222"/>
      <path d="M8 14 L26 14 L31 28 L3 28 Z" fill="#222"/>
      <circle cx="17" cy="21" r="4" fill="#666"/>
    </svg>
    <span class="phone-number">(08) 5550 0147</span>
  </div>
</header>

<div class="abs hero-band"></div>
<nav class="abs main-nav">
  <a href="#" style="left:37px">Home</a>
  <a href="#" style="left:113px">Gallery</a>
  <a href="#" style="left:215px">Order Online</a>
  <a href="#" style="left:335px">Get a quote</a>
  <a href="#" style="left:435px">Contact</a>
  <a href="#" style="left:546px">3d Visualisation</a>
  <a href="#" style="left:661px">About Us</a>
  <a href="#" style="left:757px">Sitemap</a>
</nav>
<div class="abs hero-frame"></div>
<div class="abs hero-image" role="img" aria-label="Architectural scale model of a residential housing estate with trees and streets"></div>
<div class="abs hero-caption">A picture’s worth a thousand words... a model says it all...</div>

<section class="abs intro">
  <h1>A picture’s worth a thousand words... a model says it all...</h1>
  <p>Getting an architectural model produced can be expensive and time consuming, but it can also add a lot of value to a project.&nbsp; A scale model lets everyone involved, get a very clear understanding of your building. It's this easy</p>
  <ol>
    <li>Order online or fill in the quote form.</li>
    <li>We'll build your model and deliver it right to your door.</li>
  </ol>
  <p>You can tailor your model to suit your project and budget needs.&nbsp; There are various add-ons such as a display case, internal walls, acrylic windows, people trees and cars and site contours as well as a scaled pricing structure based on the size of your building.</p>
</section>
<div class="abs divider-v"></div>
<aside class="abs why-us">
  <h2>Why Us?</h2>
  <div class="why-image" role="img" aria-label="Builder in a yellow hard hat on a building site"></div>
  <p>Lorem ipsum dolor sit amet, consectetur adipisicing elit, sed do eiusmod tempor incididunt ut labore et dolore magna aliqua...</p>
</aside>
<a class="abs read-more">Read More</a>
<div class="abs divider-h"></div>

<h2 class="abs services-title">Our Services</h2>
<div class="abs service-card card-commercial">
  <div class="service-image" role="img" aria-label="Modern commercial building with fountain plaza"></div>
  <div class="service-body"><h3>Commercial</h3><div class="service-link">Learn about our vast commercial capabilities</div></div>
</div>
<div class="abs service-card card-residential">
  <div class="service-image" role="img" aria-label="Residential complex with pool at dusk"></div>
  <div class="service-body"><h3>Residential</h3><div class="service-link">Explore our stunning residential projects</div></div>
</div>
<div class="abs service-card card-renovations">
  <div class="service-image" role="img" aria-label="Renovated two-storey yellow building"></div>
  <div class="service-body"><h3>Renovations</h3><div class="service-link">Discover Exciting renovation possibilities</div></div>
</div>

<footer class="abs site-footer">
  <div class="copyright">© Copyright The Brickfern Studio. All Rights Reserved.</div>
  <a class="social" style="left:360px" aria-label="Social link"></a>
  <a class="social" style="left:386px" aria-label="Social link"></a>
  <a class="social" style="left:413px" aria-label="Video channel link"></a>
  <a class="social" style="left:440px" aria-label="News feed link"></a>
</footer>
</body>
</html>
```